Site Update/Merger: Vortane Works

We want to take some content (not ALL the content, but only what is specified) from two or our sites and combine into one
The New Website is in Wordpress too.
The new site needs to be a nice merge between these sites:
◦ https://brevoxa-studio.example/
◦ https://taskmirel-now.example/
Theme/topic: this is an Engineering site
The blog must be included on the home page (maybe smaller), and also on the Systems Engineering page (maybe a little bigger, allow the user to browse through all blogs)
Instructions and visual aids:
Step 1: SEE BRIEFING IN THE PDF ATTACHED
Step 2: some pictures for your reference (referenced in the PDF)
Updates
The design of the children pages are not ready, and the designer still needs to load everything into my wordpress site.
Number of Pages Required
1 page
Look and feel
Each slider illustrates characteristics of the customer's brand and the style your logo design should communicate.

```html
<!DOCTYPE html>
<html lang="en">
<head>
<meta charset="utf-8">
<title>Vortane Works — Engineering Consulting</title>
<link href="https://fonts.googleapis.com/css2?family=Baloo+2:wght@400;500&family=Saira:wght@300;400;600;700&family=Roboto:wght@400;500;700&display=swap" rel="stylesheet">
<style>
:root{
  --orange:#f26522;
  --orange-deep:#d95a1c;
  --navy:#0f1a3d;
  --navy-deep:#111a3a;
  --ink:#1b1b24;
  --text:#4a4a55;
  --muted:#7b7b86;
  --white:#ffffff;
  --mist:#eef1f6;
}
*{margin:0;padding:0;box-sizing:border-box}
html,body{width:1200px;height:3419px;overflow:hidden}
body{position:relative;background:var(--white);font-family:'Roboto',sans-serif;color:var(--text)}
.abs{position:absolute}

/* header */
.site-header{position:absolute;left:0;top:0;width:1200px;height:76px;background:var(--white);border-bottom:1px solid #e6e6ea}
.brand{position:absolute;left:114px;top:14px;font-family:'Roboto',sans-serif;font-size:34px;font-weight:400;color:var(--ink);letter-spacing:0.3px}
.nav a{position:absolute;top:32px;font-family:'Saira',sans-serif;font-size:15px;color:#444;text-decoration:none;letter-spacing:0.5px}
.nav a.active{color:var(--orange)}
.nav .active-bar{position:absolute;left:587px;top:72px;width:56px;height:4px;background:var(--orange)}

/* hero */
.hero{position:absolute;left:0;top:76px;width:1200px;height:628px;background:linear-gradient(100deg,#1d3558 0%,#2e5277 45%,#4a6f93 70%,#2b4466 100%)}
.hero-shade{position:absolute;inset:0;background:linear-gradient(90deg,rgba(15,30,60,0.55) 0%,rgba(15,30,60,0.15) 60%,rgba(15,30,60,0) 100%)}
.hero .eyebrow{position:absolute;left:101px;top:196px;font-family:'Saira',sans-serif;font-size:27px;font-weight:400;color:var(--orange)}
.hero h1{position:absolute;left:101px;top:234px;width:700px;font-family:'Baloo 2',sans-serif;font-size:33px;font-weight:400;line-height:39px;color:var(--white)}

/* intro */
.intro{position:absolute;left:0;top:704px;width:1200px;height:420px;background:linear-gradient(180deg,#f1f3f8 0%,#e7ebf3 100%)}
.intro h2{position:absolute;left:100px;top:92px;font-family:'Saira',sans-serif;font-size:34px;font-weight:700;line-height:38px;color:var(--ink);text-transform:uppercase}
.intro .rule{position:absolute;left:100px;top:257px;width:50px;height:3px;background:var(--orange)}
.what-card{position:absolute;left:592px;top:63px;width:520px;height:279px;border-radius:6px;background:linear-gradient(120deg,#121a44 0%,#1a2558 55%,#25407a 100%)}
.what-card h3{position:absolute;left:46px;top:38px;font-family:'Saira',sans-serif;font-size:24px;font-weight:600;color:var(--white)}
.what-card .rule{position:absolute;left:46px;top:76px;width:46px;height:3px;background:var(--orange)}
.what-card p{position:absolute;left:46px;top:96px;width:440px;font-size:14.5px;line-height:26px;color:var(--white)}

/* section heading */
.section-title{position:absolute;left:0;width:1200px;text-align:center;font-family:'Saira',sans-serif;font-size:40px;font-weight:300;color:var(--ink)}
.section-title b{font-weight:700}
.title-rule{position:absolute;left:570px;width:60px;height:3px;background:var(--orange)}
.services-lead{position:absolute;left:190px;top:1256px;width:820px;text-align:center;font-size:18.5px;line-height:28px;color:var(--text)}

/* systems engineering */
.systems{position:absolute;left:0;top:1325px;width:1200px;height:576px;background:linear-gradient(90deg,#ffffff 0%,#ffffff 40%,#dfe9ee 62%,#b9cad6 80%,#cfd8e2 100%)}
.systems .photo{position:absolute;left:480px;top:0;width:720px;height:576px;background:linear-gradient(90deg,rgba(255,255,255,1) 0%,rgba(255,255,255,0) 30%),linear-gradient(160deg,#c7d5e0 0%,#9fb58a 50%,#e3e8ef 75%,#c9d3df 100%)}
.systems h2{position:absolute;left:121px;top:80px;font-family:'Saira',sans-serif;font-size:29px;font-weight:700;color:var(--ink)}
.systems .focus{position:absolute;left:121px;top:120px;font-size:19px;color:var(--ink)}
.value{position:absolute;left:108px;width:520px;height:86px}
.value svg{position:absolute;left:0;top:0}
.value h4{position:absolute;left:103px;top:6px;font-family:'Roboto',sans-serif;font-size:20px;font-weight:500;color:#333}
.value p{position:absolute;left:103px;top:36px;width:330px;font-size:15.5px;line-height:22px;color:var(--muted)}

/* physics */
.physics{position:absolute;left:0;top:1901px;width:1200px;height:559px}
.physics .photo{position:absolute;left:0;top:0;width:597px;height:559px;background:linear-gradient(135deg,#c9d6e3 0%,#8ea4bd 40%,#2d4764 65%,#a7b6c6 100%)}
.physics .panel{position:absolute;left:597px;top:0;width:603px;height:559px;background:linear-gradient(135deg,#f08040 0%,var(--orange) 45%,var(--orange-deep) 100%)}
.physics h2{position:absolute;left:77px;top:140px;font-family:'Saira',sans-serif;font-size:29px;line-height:31px;font-weight:300;color:var(--white)}
.physics h2 b{font-weight:700}
.physics .rule{position:absolute;left:77px;top:220px;width:50px;height:3px;background:var(--white)}
.physics p{position:absolute;left:79px;top:234px;width:440px;font-size:18px;line-height:28px;color:var(--white)}
.btn-outline{position:absolute;left:80px;top:398px;width:162px;height:45px;border:2px solid var(--white);color:var(--white);font-family:'Saira',sans-serif;font-size:15px;font-weight:600;line-height:41px;text-align:center}

/* blogs */
.blog-card{position:absolute;top:2608px;width:239px;height:349px;background:var(--white);box-shadow:0 2px 8px rgba(0,0,0,0.12)}
.blog-card .thumb{width:239px;height:188px;background:linear-gradient(135deg,#0e2f6b 0%,#1f5fb8 50%,#5aa7e6 100%)}
.blog-card .date{position:absolute;left:22px;top:203px;font-size:11px;font-weight:500;color:var(--orange)}
.blog-card h3{position:absolute;left:22px;top:221px;width:205px;font-size:14.5px;font-weight:700;line-height:22px;color:var(--ink)}
.blog-card p{position:absolute;left:22px;top:275px;width:190px;font-size:12px;line-height:17px;color:var(--muted)}

/* footer */
.site-footer{position:absolute;left:0;top:3030px;width:1200px;height:389px;background:var(--navy-deep)}
.site-footer .brand-f{position:absolute;left:121px;top:84px;font-size:35px;color:var(--white)}
.site-footer .about{position:absolute;left:121px;top:142px;width:230px;font-size:13px;line-height:20px;color:#9aa3c0}
.col-divider{position:absolute;top:0;width:1px;height:290px;background:#2a3561}
.col-mark{position:absolute;top:77px;width:3px;height:22px;background:#2f9be0}
.site-footer h4{position:absolute;top:78px;font-family:'Saira',sans-serif;font-size:15px;font-weight:600;color:var(--white)}
.site-footer ul{position:absolute;top:107px;list-style:none}
.site-footer li{font-size:13px;line-height:30px;color:#c2c8dc}
.contact-line{position:absolute;left:854px;font-size:12px;color:#c2c8dc}
.social{position:absolute;top:3200px;width:30px;height:30px;border:1.5px solid #c2c8dc;border-radius:50%}
.copyright{position:absolute;left:0;top:3378px;width:1200px;text-align:center;font-size:11px;color:#9aa3c0;letter-spacing:0.3px}
</style>
</head>
<body>

<header class="site-header">
  <div class="brand">Vortane Works</div>
  <nav class="nav">
    <a class="active" style="left:587px">HOME</a>
    <a style="left:714px">SERVICES</a>
    <a style="left:869px">CONTACT US</a>
    <span class="active-bar"></span>
  </nav>
</header>

<section class="hero" role="img" aria-label="Photo of engineers gathered around a desk reviewing technical plans">
  <div class="hero-shade"></div>
  <div class="eyebrow">WHO WE ARE</div>
  <h1>A Multi-Disciplinary Consulting<br>and Engineering Service Provider<br>for EV and Other Industries, with a Focus<br>on Systematic Product Development</h1>
</section>

<section class="intro">
  <h2>Systems Engineering<br>Solutions Modeling and<br>Hardware in the<br>Loop Consulting</h2>
  <div class="rule"></div>
  <div class="what-card" role="img" aria-label="Dark blue circuit board background">
    <h3>WHAT WE DO</h3>
    <div class="rule"></div>
    <p>A team of automotive, control and mechanical engineers from different industries and backgrounds and with more than 10 years of experience that came together to provide cost effective and specialized services to your organization or team in the pursue of your projects goals</p>
  </div>
</section>

<h2 class="section-title" style="top:1180px">OUR <b>SERVICES</b></h2>
<div class="title-rule" style="top:1228px"></div>
<p class="services-lead">This is just a glance at the activities and projects we can contribute to. For more details, go to our services menu or contact us to have a exploratory conversation.</p>

<section class="systems">
  <div class="photo" role="img" aria-label="Photo of an electric car charging with a plug connected"></div>
  <h2>SYSTEMS ENGINEERING</h2>
  <div class="focus">Our Focus: Collaboration, Accountability and Feedback</div>

  <div class="value" style="top:169px">
    <svg width="86" height="86" viewBox="0 0 86 86"><polygon points="21,6 65,6 86,43 65,80 21,80 0,43" fill="#f26522"/><circle cx="43" cy="43" r="17" fill="none" stroke="#fff" stroke-width="2.5"/></svg>
    <h4>Collaboration</h4>
    <p>Working together is the only way to maximize the team's potential</p>
  </div>
  <div class="value" style="top:282px">
    <svg width="86" height="86" viewBox="0 0 86 86"><polygon points="21,6 65,6 86,43 65,80 21,80 0,43" fill="#f26522"/><circle cx="43" cy="38" r="13" fill="none" stroke="#fff" stroke-width="2.5"/><line x1="37" y1="57" x2="49" y2="57" stroke="#fff" stroke-width="2.5"/></svg>
    <h4>Accountability</h4>
    <p>Individual contributions are paramount to the team's success</p>
  </div>
  <div class="value" style="top:384px">
    <svg width="86" height="86" viewBox="0 0 86 86"><polygon points="21,6 65,6 86,43 65,80 21,80 0,43" fill="#f26522"/><rect x="27" y="28" width="32" height="22" fill="none" stroke="#fff" stroke-width="2.5"/><line x1="22" y1="55" x2="64" y2="55" stroke="#fff" stroke-width="2.5"/><polyline points="36,39 41,44 50,34" fill="none" stroke="#fff" stroke-width="2.5"/></svg>
    <h4 style="left:106px;top:10px">Feedback</h4>
    <p style="left:106px;top:40px">Clear Feedback methods are in place</p>
  </div>
</section>

<section class="physics">
  <div class="photo" role="img" aria-label="Photo of an engineer working at a computer with car simulation screens"></div>
  <div class="panel">
    <h2>PHYSICS-BASED MODELING<br><b>AND HARDWARE IN THE LOOP</b></h2>
    <div class="rule"></div>
    <p>From data-driven system identification to real-time mathematical models for your simulation; we can handle that work for you. In addition, we are highly skilled on HIL testing and can support you in design and build phases to satisfy complex validation testing.</p>
    <div class="btn-outline">LEARN MORE</div>
  </div>
</section>

<h2 class="section-title" style="top:2505px;font-size:38px">LATEST <b>BLOGS</b></h2>
<div class="title-rule" style="top:2557px"></div>

<article class="blog-card" style="left:97px">
  <div class="thumb" role="img" aria-label="Photo of a tablet showing charts in a factory" style="background:linear-gradient(135deg,#8e9cab 0%,#3f4e63 50%,#b9c3cf 100%)"></div>
  <div class="date">25 SEPTEMBER</div>
  <h3>Fusce tellus Sed metus augue convallis et vehicula ut</h3>
  <p>Aonsectetuer augue nisi quis lacus Ut ac mi quis lacus mollis aliquam Curabitur iaculis</p>
</article>
<article class="blog-card" style="left:352px">
  <div class="thumb" role="img" aria-label="Illustration of an electric vehicle emblem on a blue circuit background"></div>
  <div class="date">25 SEPTEMBER</div>
  <h3>Fusce tellus Sed metus augue convallis et vehicula ut</h3>
  <p>Aonsectetuer augue nisi quis lacus Ut ac mi quis lacus mollis aliquam Curabitur iaculis</p>
</article>
<article class="blog-card" style="left:609px">
  <div class="thumb" role="img" aria-label="Illustration of a hand touching a digital vehicle interface"></div>
  <div class="date">25 SEPTEMBER</div>
  <h3>Fusce tellus Sed metus augue convallis et vehicula ut</h3>
  <p>Aonsectetuer augue nisi quis lacus Ut ac mi quis lacus mollis aliquam Curabitur iaculis</p>
</article>
<article class="blog-card" style="left:865px">
  <div class="thumb" role="img" aria-label="Illustration of a hand pointing at a car icon on a blue network"></div>
  <div class="date">25 SEPTEMBER</div>
  <h3>Fusce tellus Sed metus augue convallis et vehicula ut</h3>
  <p>Aonsectetuer augue nisi quis lacus Ut ac mi quis lacus mollis aliquam Curabitur iaculis</p>
</article>

<footer class="site-footer">
  <div class="brand-f">Vortane Works</div>
  <p class="about">Aonsectetuer augue nisi quis lacus Ut ac mi quis lacus mollis aliquam Curabitur iaculis</p>

  <span class="col-divider" style="left:423px"></span>
  <span class="col-mark" style="left:423px"></span>
  <h4 style="left:455px">COMPANY</h4>
  <ul style="left:454px"><li>Home</li><li>Pricing</li><li>Features</li><li>traders</li></ul>

  <span class="col-divider" style="left:616px"></span>
  <span class="col-mark" style="left:616px"></span>
  <h4 style="left:656px">RESOURCES</h4>
  <ul style="left:660px"><li>Blog</li><li>Podcast</li><li>About</li><li>Login</li></ul>

  <span class="col-divider" style="left:815px"></span>
  <span class="col-mark" style="left:815px"></span>
  <h4 style="left:853px">CONTACT US</h4>
  <div class="contact-line" style="top:112px">North America Location: Ashford Vale, SC</div>
  <div class="contact-line" style="top:136px">Email: info@taskmirel-now.example</div>
</footer>
<span class="social" style="left:856px"></span>
<span class="social" style="left:890px"></span>
<span class="social" style="left:924px"></span>
<span class="social" style="left:958px"></span>
<div class="copyright">VORTANE WORKS © 2021 ALL RIGHTS RESERVED</div>

</body>
</html>
```